Marketing Poster for Addiction Recovery Facility

We are looking for a unique marketing poster (8.5x11). We would like the poster to describe our services, and position us the industry leader in the addiction recovery health care space. - I've attached some examples as to what I would like the flyer to look like as well as attached a document listing our services and credentials.

Birchwell Healing House of Middle Tennessee
Our Phone number is 615-555-0147
Our Fax number is 615-555-0183
Physical Address - 4817 West Harlow Brook Rd
Fernvale, TN 37299
Our web address is www.birchwellhealing.example

Target Market(s)

Addiction Recovery Patients

Industry/Entity Type

Mental Health

Font styles to use
Other font styles liked:
• I'm open to the font choice, but it should be similar to the posters attached.

Colors

Designer to choose colors to be used in the design.

Requirements
Must have
• Look similar to the poster examples attached.
Nice to have
• Follow our Birchwell Healing Color Scheme
Should not have
• We are open to ideas, but it should look similar to the posters attached.

```html
<!DOCTYPE html>
<html lang="en">
<head>
<meta charset="utf-8">
<title>Birchwell Healing House of Middle Tennessee</title>
<link href="https://fonts.googleapis.com/css2?family=Alfa+Slab+One&display=swap" rel="stylesheet">
<style>
  :root {
    --cream: #f8eac5;
    --green: #1c6650;
    --tan: #d9c98a;
    --gold: #cdb465;
  }
  * { margin: 0; padding: 0; box-sizing: border-box; }
  html, body { width: 848px; height: 1200px; overflow: hidden; background: var(--cream); }
  .poster {
    position: relative; width: 848px; height: 1200px;
    background: var(--cream);
    font-family: "Alfa Slab One", Georgia, serif;
    color: var(--green);
  }
  .frame {
    position: absolute; left: 22px; top: 35px; width: 804px; height: 1130px;
    border: 25px solid var(--green);
  }
  .title {
    position: absolute; left: 0; width: 100%; text-align: center; line-height: 1; white-space: nowrap;
  }
  .title-main { top: 94px; font-size: 54px; color: var(--tan); }
  .title-sub { top: 162px; font-size: 24px; color: var(--tan); letter-spacing: 0.75em; padding-left: 0.75em; }
  .title-region { top: 192px; font-size: 57px; color: var(--green); }
  .rule { position: absolute; left: 84px; top: 266px; }
  .column {
    position: absolute; top: 336px; height: 238px; list-style: none;
  }
  .column-left { left: 90px; border-left: 2px solid var(--green); padding-left: 18px; text-align: left; }
  .column-right { right: 104px; border-right: 2px solid var(--green); padding-right: 16px; text-align: right; }
  .column h2 { font-size: 20px; font-weight: normal; color: var(--gold); line-height: 1; margin: -4px 0 12px; }
  .column li { font-size: 15.5px; line-height: 31.6px; list-style: none; white-space: nowrap; }
  .brand {
    position: absolute; left: 0; width: 100%; text-align: center; white-space: nowrap;
  }
  .brand-dot {
    position: absolute; left: 384px; top: 600px; width: 80px; height: 80px;
    border-radius: 50%; background: var(--tan);
  }
  .brand-name { top: 756px; font-size: 40px; line-height: 1; color: var(--green); }
  .brand-tagline { top: 806px; font-size: 12px; letter-spacing: 0.06em; color: var(--green); }
  .contact {
    position: absolute; left: 166px; top: 836px; width: 516px; height: 206px;
    background: var(--green); border-radius: 16px;
    box-shadow: 0 8px 10px rgba(0,0,0,0.35);
    color: var(--cream);
  }
  .contact h2 { position: absolute; left: 104px; top: 20px; font-size: 40px; font-weight: normal; line-height: 1; }
  .contact-line { position: absolute; left: 104px; font-size: 16px; line-height: 1; white-space: nowrap; }
  .icon { position: absolute; left: 56px; }
  .website {
    position: absolute; left: 0; top: 1076px; width: 100%; text-align: center;
    font-size: 29px; line-height: 1; color: var(--green); white-space: nowrap;
  }
</style>
</head>
<body>
<main class="poster">
  <div class="frame"></div>

  <h1 class="title title-main">BIRCHWELL HEALING</h1>
  <p class="title title-sub">HOUSE OF</p>
  <p class="title title-region">MIDDLE TENNESSEE</p>
  <svg class="rule" width="680" height="8" viewBox="0 0 680 8" aria-hidden="true">
    <path d="M0 4 Q340 -1 680 4 Q340 9 0 4 Z" fill="var(--green)"/>
  </svg>

  <section class="column column-left">
    <h2>TREATMENT SERVICES</h2>
    <ul>
      <li>MEDICATION ASSISTED</li>
      <li>OPIOID TREATMENT</li>
      <li>INDIVIDUAL COUNSELING</li>
      <li>GROUP THERAPY</li>
      <li>FAMILY COUNSELING</li>
      <li>SERVICES</li>
      <li>GAMBLING ADDICTION</li>
    </ul>
  </section>

  <section class="column column-right">
    <h2>CREDENTIALS</h2>
    <ul>
      <li>LICENSED OFFICE BASED</li>
      <li>OPIATE TREATMENT FACILITY</li>
      <li>LICENSED PROFESSIONAL</li>
      <li>COUNSELORS</li>
      <li>BOARD CERTIFIED</li>
      <li>ADDICTIONOLOGIST</li>
    </ul>
  </section>

  <div class="brand-dot" aria-hidden="true"></div>
  <p class="brand brand-name">BIRCHWELL HEALING</p>
  <p class="brand brand-tagline">MIDDLE TENNESSEE'S ADDICTION RECOVERY CENTER</p>

  <section class="contact">
    <h2>CONTACT</h2>
    <svg class="icon" style="top:66px" width="24" height="26" viewBox="0 0 24 26" aria-label="Phone">
      <rect x="1" y="1" width="22" height="24" rx="4" fill="var(--cream)"/>
      <path d="M8 6 C6 8 6 12 9 16 C12 20 15 21 17 20 L16 17 L13.5 17.5 C12 16 10.5 13.5 10 11.5 L12 10 L10.5 6.5 Z" fill="var(--green)"/>
    </svg>
    <span class="contact-line" style="top:68px">615-555-0147</span>
    <span class="contact-line" style="top:102px">615-555-0183</span>
    <svg class="icon" style="top:153px" width="32" height="14" viewBox="0 0 32 14" aria-label="Address">
      <path d="M0 4 H18 V0 L32 7 L18 14 V10 H0 Z" fill="var(--cream)"/>
    </svg>
    <span class="contact-line" style="top:135px">FERNVALE, TN 37299</span>
    <span class="contact-line" style="top:170px">4817 WEST HARLOW BROOK RD</span>
  </section>

  <p class="website">WWW.BIRCHWELLHEALING.EXAMPLE</p>
</main>
</body>
</html>
```